Online radio: Zintavox homepage redesign

Zintavox is one of the world's leading brands of personalizable online radio -- similar to Kelvessa, but aimed at a somewhat older audience (age 35-54).

We'd like to redesign our homepage with a more contemporary look: It should emphasize our wide variety of GENRES (as the primary navigation), with the search field easy to find as a secondary navigation.

We'd like to retain our corporate color of maroon/plum. (We are not committed to the gold/yellow secondary color.)

See our current homepage at www.zintavox.com and our in-house attempt at an improved design at http://web4.zintavox.com/finder/2013ms/.

Ideally, we'd like to see designs for up to THREE different states:

(1) An initial state when users first come to the page.

(2) What the page would look like as the user is looking at channel options.

(3) What the page would look like once the media player is launched.

However, you may be able to combine (2) and (3) in a single screenshot.

Thanks!

At the request of several designers, we have decided to extend our deadline by four days. At the same time, we have increased our budget, including the addition of a 2nd place award. Thanks for your excellent work!

Reason: Extended at the request of a couple of designers. May mean you don't have to work over the weekend!

Thanks very much for your designs! We are very pleased with the overall quality of the work we are seeing. One reminder: As our brief says, the user interface "should emphasize our wide variety of GENRES (as the primary navigation), with the search field easy to find as a secondary navigation," and we feel that your design uses the SEARCH field as the primary navigation. Many of the designs use a large search field as the primary navigation. If yours does, you might want to tweak your design to put a greater emphasis on browsing genres as the primary navigation. Thanks and good luck!

Target Market(s)

Adults age 35-54 listening to online radio at work

Industry/Entity Type

Radio

Font styles to use
Sans Serif

Requirements
Must have
• This is a design/UI project -- we do not need code

```html
<!DOCTYPE html>
<html lang="en">
<head>
<meta charset="utf-8">
<title>Zintavox – Online Radio</title>
<link href="https://fonts.googleapis.com/css2?family=Source+Sans+3:ital,wght@0,400;0,600;0,700;1,400&display=swap" rel="stylesheet">
<style>
  :root {
    --plum: #5c0b56;
    --plum-dark: #4a0845;
    --page: #f1f0f1;
    --ink: #222222;
    --muted: #6b6b6b;
    --line: #d6d6d6;
    --footer: #1c1c1c;
    --white: #ffffff;
    --accent: #f5d21c;
  }
  * { box-sizing: border-box; margin: 0; padding: 0; }
  html, body { width: 952px; height: 1200px; overflow: hidden; }
  body {
    position: relative;
    background: var(--page);
    font-family: "Source Sans 3", "Helvetica Neue", Arial, sans-serif;
    color: var(--ink);
  }
  .abs { position: absolute; }

  .masthead { position: absolute; left: 0; top: 0; width: 952px; height: 339px; background: var(--plum); }
  .brand { left: 109px; top: 26px; display: flex; align-items: center; gap: 8px; color: var(--white); font-size: 29px; font-weight: 600; letter-spacing: -0.5px; }
  .brand-dot { width: 34px; height: 34px; border-radius: 50%; background: var(--accent); }
  .account { right: 100px; top: 16px; font-size: 9px; font-weight: 700; color: var(--white); display: flex; gap: 5px; }
  .account .sep { opacity: .6; font-weight: 400; }
  .main-nav { top: 62px; left: 583px; display: flex; gap: 24px; font-size: 14px; color: var(--white); }

  .hero { left: 102px; top: 91px; width: 750px; height: 355px;
    background:
      radial-gradient(ellipse 22% 28% at 53% 22%, rgba(200,110,70,.75) 0%, rgba(200,110,70,0) 100%),
      radial-gradient(ellipse 18% 22% at 22% 38%, rgba(120,150,70,.45) 0%, rgba(120,150,70,0) 100%),
      radial-gradient(ellipse 16% 20% at 70% 20%, rgba(60,140,150,.4) 0%, rgba(60,140,150,0) 100%),
      radial-gradient(ellipse 30% 30% at 45% 85%, rgba(170,140,110,.45) 0%, rgba(170,140,110,0) 100%),
      radial-gradient(ellipse at 50% 45%, #6e4a46 0%, #54494a 45%, #403f42 100%); }
  .hero-title { left: 102px; top: 202px; width: 750px; text-align: center; color: var(--white); font-size: 35px; font-weight: 400; letter-spacing: .2px; }
  .search { left: 251px; top: 302px; width: 450px; height: 62px; background: var(--white); border-radius: 6px; box-shadow: 0 2px 6px rgba(0,0,0,.35); display: flex; }
  .search-field { flex: 1; display: flex; align-items: center; padding-left: 39px; font-size: 17px; font-style: italic; color: #9a9a9a; border-right: 1px solid var(--line); }
  .search-btn { width: 81px; display: flex; align-items: center; justify-content: center; }
  .hero-shadow { left: 140px; top: 446px; width: 674px; height: 34px; background: radial-gradient(ellipse at 50% 0%, rgba(0,0,0,.28) 0%, rgba(0,0,0,0) 70%); }

  .side-btn { left: 100px; width: 139px; height: 29px; border-radius: 3px; display: flex; align-items: center; font-size: 14px; }
  .side-btn .label { flex: 1; text-align: center; }
  .side-btn .caret { width: 42px; height: 100%; display: flex; align-items: center; justify-content: center; }
  .dj { top: 505px; background: var(--plum); color: var(--white); border: 1px solid var(--plum-dark); }
  .dj .label { text-align: left; padding-left: 23px; }
  .plain { background: #ececec; border: 1px solid var(--line); color: #444; }
  .plain .caret { border-left: 1px solid var(--line); }
  .menu { left: 110px; top: 541px; width: 121px; height: 72px; background: #f7f7f7; border: 1px solid var(--line); border-radius: 3px; }
  .menu div { height: 23px; display: flex; align-items: center; padding-left: 10px; font-size: 7px; color: var(--muted); border-bottom: 1px solid var(--line); }
  .menu div:last-child { border-bottom: none; }
  .menu .active { color: var(--plum); font-weight: 600; }

  .genre { width: 155px; text-align: center; }
  .covers { display: flex; gap: 2px; height: 50px; }
  .covers span { flex: 1; }
  .genre h3 { font-weight: 400; font-size: 17.5px; margin-top: 10px; color: var(--ink); letter-spacing: .2px; }

  .c-pop1 { background: linear-gradient(160deg, #f1e632 0%, #e3d21e 100%); }
  .c-pop2 { background: linear-gradient(170deg, #8a7a66 0%, #5e4e3c 60%, #7c6a52 100%); }
  .c-pop3 { background: linear-gradient(175deg, #d6a838 0%, #b5852a 55%, #6a4a22 100%); }
  .c-lite1 { background: linear-gradient(160deg, #b5906e 0%, #7a5a44 60%, #c8b060 100%); }
  .c-lite2 { background: linear-gradient(180deg, #7ab2be 0%, #3e6c78 55%, #6a5a40 100%); }
  .c-lite3 { background: linear-gradient(160deg, #b8c4cc 0%, #8a9aa4 50%, #c4a870 100%); }
  .c-cty1 { background: linear-gradient(180deg, #2c2624 0%, #4a3c34 60%, #2a2422 100%); }
  .c-cty2 { background: linear-gradient(170deg, #e4e0da 0%, #b8b2a8 100%); }
  .c-cty3 { background: linear-gradient(170deg, #6a4a30 0%, #3e5a22 60%, #1e2a10 100%); }
  .c-cls1 { background: linear-gradient(170deg, #3a3230 0%, #1c1816 100%); }
  .c-cls2 { background: linear-gradient(170deg, #8a6048 0%, #4a3024 100%); }
  .c-cls3 { background: linear-gradient(170deg, #4a4a4c 0%, #222224 100%); }
  .c-rock1 { background: linear-gradient(170deg, #7a8688 0%, #3e4648 100%); }
  .c-rock2 { background: linear-gradient(170deg, #d6a040 0%, #8a6a32 55%, #3a5a7a 100%); }
  .c-rock3 { background: linear-gradient(170deg, #d8b890 0%, #a07450 100%); }
  .c-jazz1 { background: linear-gradient(170deg, #9a3030 0%, #5a1a1a 100%); }
  .c-jazz2 { background: linear-gradient(170deg, #eeece8 0%, #bdbab4 100%); }
  .c-jazz3 { background: linear-gradient(170deg, #6a6a6c 0%, #2e2e30 100%); }

  .load-more { left: 487px; top: 903px; width: 158px; height: 50px; background: var(--plum); color: var(--white); border-radius: 3px; display: flex; align-items: center; justify-content: center; font-size: 18px; font-weight: 600; }

  .footer { left: 0; top: 1032px; width: 952px; height: 168px; background: var(--footer); color: var(--white); }
  .footer h4 { position: absolute; left: 122px; top: 17px; font-size: 18px; font-weight: 600; }
  .quick-links { position: absolute; left: 122px; top: 52px; width: 672px; font-size: 13.6px; line-height: 16px; }
  .copyright { position: absolute; left: 124px; top: 143px; font-size: 8.5px; }
  .social { position: absolute; left: 701px; top: 140px; display: flex; gap: 6px; }
  .social span { width: 20px; height: 20px; border-radius: 50%; background: #050505; }
</style>
</head>
<body>
  <header class="masthead">
    <div class="abs brand"><span class="brand-dot"></span>Zintavox</div>
    <div class="abs account"><span>Log In</span><span class="sep">|</span><span>Sign Up</span></div>
    <nav class="abs main-nav"><span>Home</span><span>About &amp; Contact</span><span>Help</span><span>Mobile</span></nav>
  </header>

  <div class="abs hero" role="img" aria-label="Photo of a woman with red hair wearing headphones amid colourful paint splashes"></div>
  <h1 class="abs hero-title">Thousands of radio stations with endless music</h1>
  <div class="abs search">
    <div class="search-field">Search by artist or keyword</div>
    <div class="search-btn">
      <svg width="34" height="34" viewBox="0 0 34 34"><circle cx="13" cy="13" r="9" fill="none" stroke="#5c0b56" stroke-width="4"/><line x1="20" y1="20" x2="31" y2="30" stroke="#5c0b56" stroke-width="5" stroke-linecap="round"/></svg>
    </div>
  </div>
  <div class="abs hero-shadow"></div>

  <div class="abs side-btn dj"><span class="label">DJ Picks</span><span class="caret"><svg width="14" height="11"><path d="M0 0h14L7 11z" fill="#fff"/></svg></span></div>
  <div class="abs menu">
    <div>Most Popular Channels</div>
    <div class="active">Get Motivated</div>
    <div>Concentrate</div>
  </div>
  <div class="abs side-btn plain" style="top:637px"><span class="label">Genres</span><span class="caret"><svg width="13" height="10"><path d="M0 0h13L6.5 10z" fill="#222"/></svg></span></div>
  <div class="abs side-btn plain" style="top:673px"><span class="label">Surprise Me</span><span class="caret"><svg width="13" height="10"><path d="M0 0h13L6.5 10z" fill="#222"/></svg></span></div>

  <div class="abs genre" style="left:289px;top:535px"><div class="covers" role="img" aria-label="Album covers for top 40 and pop hits"><span class="c-pop1"></span><span class="c-pop2"></span><span class="c-pop3"></span></div><h3>Top 40 / Pop Hits</h3></div>
  <div class="abs genre" style="left:481px;top:535px"><div class="covers" role="img" aria-label="Album covers for lite hits"><span class="c-lite1"></span><span class="c-lite2"></span><span class="c-lite3"></span></div><h3>Lite Hits</h3></div>
  <div class="abs genre" style="left:673px;top:535px"><div class="covers" role="img" aria-label="Album covers for country"><span class="c-cty1"></span><span class="c-cty2"></span><span class="c-cty3"></span></div><h3>Country</h3></div>

  <div class="abs genre" style="left:289px;top:644px"><div class="covers" role="img" aria-label="Album covers for classical"><span class="c-cls1"></span><span class="c-cls2"></span><span class="c-cls3"></span></div><h3>Classical</h3></div>
  <div class="abs genre" style="left:481px;top:644px"><div class="covers" role="img" aria-label="Album covers for classic rock"><span class="c-rock1"></span><span class="c-rock2"></span><span class="c-rock3"></span></div><h3>Classic Rock</h3></div>
  <div class="abs genre" style="left:673px;top:644px"><div class="covers" role="img" aria-label="Album covers for smooth jazz"><span class="c-jazz1"></span><span class="c-jazz2"></span><span class="c-jazz3"></span></div><h3>Smooth Jazz</h3></div>

  <div class="abs genre" style="left:289px;top:765px"><div class="covers" role="img" aria-label="Album covers for top 40 and pop hits"><span class="c-pop1"></span><span class="c-pop2"></span><span class="c-pop3"></span></div><h3>Top 40 / Pop Hits</h3></div>
  <div class="abs genre" style="left:481px;top:765px"><div class="covers" role="img" aria-label="Album covers for lite hits"><span class="c-lite1"></span><span class="c-lite2"></span><span class="c-lite3"></span></div><h3>Lite Hits</h3></div>
  <div class="abs genre" style="left:673px;top:765px"><div class="covers" role="img" aria-label="Album covers for country"><span class="c-cty1"></span><span class="c-cty2"></span><span class="c-cty3"></span></div><h3>Country</h3></div>

  <div class="abs load-more">Load more</div>

  <footer class="abs footer">
    <h4>QUICK LINKS</h4>
    <p class="quick-links">•My History •My Favorites •Most Popular •Workday Mood •Great Summer Music • Get Motivated • Concentrate •Almost 5 O'ClockRelax and Unwind •Adult • Alternative •Rock Adult •Contemporary• &nbsp;'50sDecade •'60sDecade • '70sDecade• '80sDecade • '90sDecade</p>
    <p class="copyright">©Zintavox2014. All Rights Reserved</p>
    <div class="social" aria-label="Social links"><span></span><span></span><span></span><span></span><span></span><span></span></div>
  </footer>
</body>
</html>
```